Institutional website for an IT Consulting company

Web design + HTML + CSS / Bootstrap + JS (interaction) integration in order to extend our existing website brisklane.coop.
Our website is currently aiming only for recruitment and not for customers, we want to provide a fluid transition between customer side website (this project) and recruitment website (existing site).

Ideally we would love the new design to be "inspired" by our actual graphic chart (Colors mainly). It should provide a great user experience and a landing page (or any mean) allowing the visitor to easily switch from the end customer front end (this project), the recruitment front end (existing front end https://www.brisklane.coop/) and the existing member front end (an other existing front end dedicated to members already existing).

In attachment you will find the expected site content mainly a one page with a first level of information and "link" to sub pages (a way to directly access this sub pages should also be provided).

The website should be accessible on mobile device and desktop.

The attachment is in french as it reflect the final site content, but if google translate isn't sufficient to have a general idea of the content, feel free to ask. We would love to have some visual representation for some categories.

Target Market(s)

fortune 500 companies

Industry/Entity Type

It Company

Coding

Coded - Design and coding required

Number of Pages Required

5+ page

Requirements
Must have
• This project must have an easy way to navigate between 3 sub sites, the customer one (the one designed here), the consultant / recruitment one (the existing one at brisklane.coop), the members one.

A one page experience at first leading to detail pages.

Custom made visuals to illustrate each categories.

Inspiration websites : plovu[.]fr ; tarnsby[.]com ; qolvari[.] com ...

Be inspired by the existing color from our logo and existing website at brisklane[.]coop

```html
<!DOCTYPE html>
<html lang="fr">
<head>
<meta charset="utf-8">
<title>Brisklane.coop</title>
<link href="https://fonts.googleapis.com/css2?family=Montserrat:wght@400;600;700;800&family=Karla:wght@400;500;700&display=swap" rel="stylesheet">
<style>
:root{
  --teal-dark:#0e4a48;
  --accent:#2bb3c0;
  --ink:#1f2426;
  --muted:#444b4e;
  --grey-bg:#f7f7f7;
  --card:#f4f4f4;
  --line:#d9dcdd;
  --white:#ffffff;
}
*{box-sizing:border-box;margin:0;padding:0}
html,body{width:1200px;height:2884px;overflow:hidden}
body{position:relative;background:var(--white);font-family:"Karla",sans-serif;color:var(--ink)}
.abs{position:absolute}
.brand{font-family:"Montserrat",sans-serif;font-weight:800;font-size:30px;letter-spacing:.5px;color:var(--teal-dark);display:flex;align-items:center;gap:8px}
.brand .mark{width:14px;height:14px;background:var(--accent)}
.nav{display:flex;gap:27px;font-family:"Montserrat",sans-serif;font-weight:700;font-size:13px;color:var(--teal-dark)}
.nav .active{color:var(--accent)}
.btn{position:absolute;display:flex;align-items:center;gap:14px;height:41px;padding:0 18px 0 0;border:2px solid var(--accent);background:var(--white);font-family:"Montserrat",sans-serif;font-weight:700;font-size:14px;color:var(--ink);text-transform:uppercase}
.btn .sq{width:20px;height:28px;background:var(--teal-dark);border-left:4px solid var(--accent);margin-left:0}
.photo{position:absolute;left:0;width:1200px}
.hero{top:0;height:600px;background:linear-gradient(100deg,#c9b8a4 0%,#a07c5d 30%,#d4b897 55%,#8f6a47 80%,#e2cfb8 100%)}
.intro-card{position:absolute;top:529px;width:338px;padding:22px 22px 0;background:linear-gradient(to bottom,rgba(255,255,255,.88),#fff 60px);font-size:16px;font-weight:700;line-height:20px;color:var(--ink);height:160px}
.grey{top:780px;height:530px;background:var(--grey-bg)}
.lead{position:absolute;top:850px;left:0;width:1200px;text-align:center;font-family:"Montserrat",sans-serif;font-size:20px;line-height:25px;color:var(--muted)}
.lead b{color:var(--ink)}
.lead em{font-style:normal;font-weight:600;color:var(--accent)}
.bar{position:absolute;height:7px;width:214px;border:2px solid var(--accent);border-radius:4px}
.h2{position:absolute;left:0;width:1200px;text-align:center;font-family:"Montserrat",sans-serif;font-weight:600;font-size:21px;color:var(--ink)}
.topic{position:absolute;width:300px;text-align:center;font-size:16px;font-weight:500;line-height:20px;color:var(--ink)}
.topic svg{display:block;margin:0 auto 14px}
.band1{top:1310px;height:316px;background:linear-gradient(90deg,#f1efed 0%,#e7e3df 25%,#2d4b74 45%,#3a5680 65%,#c9a98a 85%,#efe5da 100%)}
.band-title{position:absolute;font-family:"Montserrat",sans-serif;font-size:38px;line-height:40px;color:var(--ink)}
.band-title b{font-weight:800}
.band2{top:1938px;height:316px;background:linear-gradient(90deg,#7a8a96 0%,#a9b6c2 25%,#e6a679 40%,#9fb1c3 60%,#dfe5ea 85%,#eef1f4 100%)}
.contact-card{position:absolute;left:88px;top:2326px;width:352px;height:289px;background:var(--card)}
.contact-card h3,.form-title{font-family:"Montserrat",sans-serif;font-weight:700;font-size:20px;color:var(--ink);text-align:center}
.info{position:absolute;left:44px;display:flex;gap:8px;font-size:15px;font-weight:700;line-height:19px;color:var(--ink)}
.field{position:absolute;border:1px solid var(--line);background:var(--white);font-size:15px;color:var(--muted);padding:9px 15px}
.footer{position:absolute;top:2686px;left:0;width:1200px;height:198px;background:var(--teal-dark)}
.footer .brand{color:var(--white)}
.footer .nav{color:var(--white)}
.social{display:flex;gap:20px}
.social span{width:12px;height:12px;border-radius:50%;border:1.5px solid #8fb3b2}
.copy{font-family:"Montserrat",sans-serif;font-size:9px;font-weight:600;color:#a8c3c2}
</style>
</head>
<body>

<header>
  <div class="photo hero" role="img" aria-label="Équipe de consultants travaillant ensemble autour d'un ordinateur portable"></div>
  <div class="abs brand" style="left:69px;top:40px">BRISKLANE.COOP <span class="mark"></span></div>
  <nav class="abs nav" style="right:72px;top:52px">
    <span class="active">HOME</span><span>CAE-SCOP</span><span>DE RECHERCHE</span><span>DES EXPERTS DE LEUR DOMAINE</span><span>ACTUALITÉ ET CLIENTS</span>
  </nav>
</header>

<section>
  <div class="intro-card" style="left:70px">Brisklane.coop est une société de services avec des valeurs fortes de coopération, reposant notamment sur une organisation atypique.</div>
  <div class="btn" style="left:91px;top:648px"><span class="sq"></span>CAE-SCOP</div>
  <div class="intro-card" style="left:431px;top:551px">Nous disposons de profils de autonomes sur les sujets Cirrus BI, infrastructure et sécurité, Data Plateforme!</div>
  <div class="btn" style="left:451px;top:669px"><span class="sq"></span>DE RECHERCHE</div>
  <div class="intro-card" style="left:790px">Mais pourquoi opter pour un seul consultant quand Brisklane.coop vous propose toute une communauté à votre service!</div>
  <div class="btn" style="left:807px;top:648px"><span class="sq"></span>DES EXPERTS DE LEUR DOMAINE</div>
</section>

<section>
  <div class="photo grey"></div>
  <p class="lead"><b>Brisklane</b> c'est avant tout un ensemble un regroupement <em>d'experts</em> incluant notamment<br>plusieurs MVP, en coopération étroite avec l'ensemble des consultants au quotidien</p>
  <div class="bar" style="left:493px;top:913px"></div>
  <h2 class="h2" style="top:956px">À titre d'exemple, nous pouvons intervenir sur les sujets suivants</h2>

  <div class="topic" style="left:125px;top:1005px">
    <svg width="62" height="66" viewBox="0 0 62 66" fill="none" stroke="var(--teal-dark)" stroke-width="2.5"><ellipse cx="31" cy="33" rx="29" ry="11"/><ellipse cx="31" cy="33" rx="29" ry="11" transform="rotate(60 31 33)"/><ellipse cx="31" cy="33" rx="29" ry="11" transform="rotate(120 31 33)"/><circle cx="31" cy="33" r="6" stroke="var(--accent)"/></svg>
    Architecture hybride</div>
  <div class="topic" style="left:450px;top:1005px">
    <svg width="66" height="66" viewBox="0 0 66 66" fill="none" stroke="var(--teal-dark)" stroke-width="2.5"><circle cx="33" cy="33" r="18"/><rect x="25" y="31" width="16" height="12" rx="2"/><path d="M28 31v-5a5 5 0 0 1 10 0v5"/><circle cx="8" cy="8" r="5" fill="var(--accent)" stroke="none"/><circle cx="58" cy="8" r="5" fill="var(--accent)" stroke="none"/><circle cx="8" cy="58" r="5" fill="var(--accent)" stroke="none"/><circle cx="58" cy="58" r="5" fill="var(--accent)" stroke="none"/><path d="M12 12l8 8M54 12l-8 8M12 54l8-8M54 54l-8-8"/></svg>
    Sécurité et infrastructure</div>
  <div class="topic" style="left:775px;top:1005px">
    <svg width="58" height="66" viewBox="0 0 58 66" fill="none" stroke="var(--teal-dark)" stroke-width="2.5"><ellipse cx="29" cy="8" rx="26" ry="6"/><path d="M3 8v50c0 3 12 6 26 6s26-3 26-6V8"/><path d="M3 24c0 3 12 6 26 6s26-3 26-6M3 41c0 3 12 6 26 6s26-3 26-6"/><circle cx="29" cy="37" r="3" fill="var(--accent)" stroke="none"/><circle cx="29" cy="54" r="3" fill="var(--accent)" stroke="none"/></svg>
    Expertise modern data warehouse</div>

  <div class="topic" style="left:125px;top:1125px">
    <svg width="60" height="62" viewBox="0 0 60 62" fill="none" stroke-width="2.5"><rect x="6" y="2" width="52" height="56" rx="3" stroke="var(--teal-dark)"/><g fill="var(--accent)"><rect x="2" y="36" width="7" height="18"/><rect x="12" y="28" width="7" height="26"/><rect x="22" y="20" width="7" height="34"/><rect x="32" y="12" width="7" height="42"/></g></svg>
    Visualisation avancée notamment<br>via Lumen BI</div>
  <div class="topic" style="left:464px;top:1125px">
    <svg width="62" height="62" viewBox="0 0 62 62"><rect x="8" y="8" width="46" height="46" rx="6" fill="var(--teal-dark)"/><circle cx="31" cy="31" r="10" fill="var(--accent)"/></svg>
    Rasionalisation de vos<br>coûts Cirrus</div>
  <div class="topic" style="left:775px;top:1125px">
    <svg width="62" height="62" viewBox="0 0 62 62" fill="none" stroke="var(--teal-dark)" stroke-width="2"><rect x="26" y="4" width="32" height="24"/><path d="M34 22v-6M40 22v-9M46 22v-12M52 22v-15" stroke="var(--accent)"/><circle cx="14" cy="14" r="5"/><path d="M6 34c0-6 4-10 8-10s8 4 8 10"/><circle cx="14" cy="42" r="5"/><circle cx="31" cy="42" r="5"/><circle cx="48" cy="42" r="5"/><path d="M5 60c0-6 4-9 9-9s9 3 9 9M22 60c0-6 4-9 9-9s9 3 9 9M39 60c0-6 4-9 9-9s9 3 9 9"/></svg>
    Formations</div>
</section>

<section>
  <div class="photo band1" role="img" aria-label="Mains d'une équipe tenant une tablette et des documents"></div>
  <h2 class="band-title" style="left:90px;top:1398px"><b>Vous souhaitez</b><br>un devis</h2>
  <div class="btn" style="left:91px;top:1495px"><span class="sq"></span>ADRESSE COMMERCIALE</div>
</section>

<section>
  <h2 class="h2" style="top:1697px">Nos équipes sont fortement orientées Cirrus sur les thématiques</h2>
  <div class="bar" style="left:493px;top:1731px"></div>
  <div class="topic" style="left:306px;top:1777px">
    <svg width="66" height="60" viewBox="0 0 66 60" fill="none" stroke="var(--teal-dark)" stroke-width="2"><path d="M33 4L63 20L33 36L3 20Z"/><path d="M3 30l30 16 30-16"/><path d="M3 40l30 16 30-16" stroke="var(--accent)" stroke-dasharray="3 3"/></svg>
    Data plateforme</div>
  <div class="topic" style="left:593px;top:1772px">
    <svg width="62" height="66" viewBox="0 0 62 66" fill="none" stroke="var(--teal-dark)" stroke-width="2"><circle cx="17" cy="5" r="4" stroke="var(--accent)"/><rect x="4" y="14" width="54" height="40"/><rect x="9" y="19" width="54" height="40" stroke="var(--line)"/><path d="M26 26h10v6H26zM14 40h10v6H14zM38 40h10v6H38zM31 32v4H19v4M31 36h12v4"/><circle cx="52" cy="61" r="4" stroke="var(--accent)"/></svg>
    Data and BI</div>
</section>

<section>
  <div class="photo band2" role="img" aria-label="Main tenant une ampoule lumineuse entourée d'un réseau de points connectés"></div>
  <h2 class="band-title" style="left:781px;top:2048px;font-size:35px"><b>Ou en savoir plus?</b></h2>
  <div class="btn" style="left:782px;top:2106px"><span class="sq"></span>CONTACTEZ-NOUZ</div>
</section>

<section>
  <div class="contact-card">
    <h3 style="margin-top:36px">Contactez-nous!</h3>
    <div class="bar" style="left:78px;top:74px"></div>
    <div class="info" style="top:118px"><svg width="12" height="16" viewBox="0 0 12 16"><path d="M6 0a6 6 0 0 1 6 6c0 4-6 10-6 10S0 10 0 6a6 6 0 0 1 6-6z" fill="var(--accent)"/><circle cx="6" cy="6" r="2" fill="#fff"/></svg><span>BRISKLANE.COOP - COWORKHUB<br>12 Rue des Tanneurs 75011<br>Paris</span></div>
    <div class="info" style="top:197px"><svg width="14" height="14" viewBox="0 0 14 14"><path d="M2 1l3 0 1 4-2 1a8 8 0 0 0 4 4l1-2 4 1v3c-7 1-12-4-11-11z" fill="var(--accent)"/></svg><span>Téléphone : 01 84 60 27 15</span></div>
    <div class="info" style="top:238px;font-weight:500"><svg width="14" height="12" viewBox="0 0 14 12"><rect x="0" y="1" width="14" height="10" fill="var(--accent)"/><path d="M0 1l7 6 7-6" stroke="#fff" fill="none"/></svg><span>info@brisklane.coop</span></div>
  </div>

  <h3 class="abs form-title" style="left:515px;top:2325px;width:597px">Ecrivez-nous</h3>
  <div class="bar" style="left:706px;top:2364px"></div>
  <div class="field" style="left:515px;top:2400px;width:294px;height:39px">Votre Nom</div>
  <div class="field" style="left:818px;top:2400px;width:294px;height:39px">Votre Email</div>
  <div class="field" style="left:515px;top:2450px;width:597px;height:116px">Votre Message</div>
  <div class="btn" style="left:708px;top:2575px;font-size:13px"><span class="sq"></span>ENVOYER LE MESSAGE</div>
</section>

<footer class="footer">
  <div class="abs brand" style="left:69px;top:56px">BRISKLANE.COOP <span class="mark"></span></div>
  <nav class="abs nav" style="right:72px;top:66px">
    <span class="active">HOME</span><span>CAE-SCOP</span><span>DE RECHERCHE</span><span>DES EXPERTS DE LEUR DOMAINE</span><span>ACTUALITÉ ET CLIENTS</span>
  </nav>
  <div class="abs social" style="left:92px;top:134px"><span></span><span></span><span></span><span></span><span></span></div>
  <div class="abs copy" style="right:72px;top:136px">© 2020 BRISKLANE.COOP - ALL RIGHTS RESERVED</div>
</footer>

</body>
</html>
```